依頼詳細
エステサロン、SPA施設、百貨店、雑貨屋などの店頭でも陳列できるようなシンプルかつおしゃれで女性に好感が持てるようなデザインを希望します。
またホームセンターやドラックストアなどで販売されているような商品に比べて高価になる為、高級感があるデザインを希望します。

シリカは水晶(クリスタル)から抽出しているので、水晶のマーク、イラストなどを入れたいです。
本製品は、雑貨ではなく「化粧品」としての販売となります。

ミストヘイブンと水晶の写真は添付資料をご確認ください。
記載項目
ボトルサイズD78㎜×H160㎜(添付参照)
印刷:4C
材質:シュリンクフィルムPP
希望イメージ
シンプル 複雑
単色 カラフル
暗い 明るい
日常 高級
遊び心 厳粛
未来的 伝統的
女性的 男性的
希望する色
青系、水色系
納品ファイル
• 高解像度JPG (.jpg)
• イラストレーター形式 (.ai)
補足説明
変更で申し訳ございませんが、
水晶(シリカ)のロゴはなしでお願いいたします。
アイスランドにあるミストヘイブンのイメージで
高級感のあるデザインを希望します。
よろしくお願いいたします。
■ 選んだ理由

ミストヘイブンのイメージが湧きやすくイメージに近かったため選ばせて頂きました。

■ 提案者全員のお礼・コメント

この度はたくさんのご提案を頂戴し誠にありがとうございました。
どれも素敵なデザインで選定に悩みました。
また機会があればご参加いただけますと幸いです。
この度はありがとうございました。

```html
<!DOCTYPE html>
<html lang="ja">
<head>
<meta charset="utf-8">
<title>Aurora Serene Bath Salt Label</title>
<link href="https://fonts.googleapis.com/css2?family=Cinzel:wght@400&family=Noto+Sans+JP:wght@400;500&family=Lato:wght@400&display=swap" rel="stylesheet">
<style>
  :root {
    --page: #ffffff;
    --cap: #f4f4f1;
    --cap-edge: #dcdcd6;
    --sky-deep: #5797c6;
    --sky-mid: #8fbddc;
    --sky-pale: #d6e8f2;
    --ridge: #35617f;
    --ridge-light: #7ea7c0;
    --lagoon: #8fd0d8;
    --lagoon-pale: #c9e9ee;
    --mist: #eaf6f8;
    --ink-light: #ffffff;
    --ink-soft: rgba(255,255,255,0.9);
    --band: rgba(255,255,255,0.85);
    --band-ink: #3f86b0;
  }
  html, body {
    margin: 0; padding: 0;
    width: 718px; height: 1200px;
    overflow: hidden;
    background: var(--page);
  }
  .label { position: relative; width: 718px; height: 1200px; }
  .label__bottle { position: absolute; inset: 0; }
  .label__mark {
    position: absolute;
    left: 337px; top: 318px;
    width: 44px; height: 44px;
    border: 3px solid var(--ink-light);
    box-sizing: border-box;
  }
  .label__name {
    position: absolute;
    left: 0; width: 718px;
    margin: 0;
    text-align: center;
    font-family: "Cinzel", serif;
    font-weight: 400;
    font-size: 70px;
    letter-spacing: 5px;
    line-height: 1;
    color: var(--ink-light);
  }
  .label__name--first { top: 410px; }
  .label__name--second { top: 490px; }
  .label__reading {
    position: absolute;
    left: 444px; top: 562px;
    font-family: "Noto Sans JP", sans-serif;
    font-size: 12px;
    letter-spacing: 3px;
    color: var(--ink-soft);
  }
  .label__claim {
    position: absolute;
    left: 221px; top: 670px;
    width: 278px; height: 40px;
    background: var(--band);
    color: var(--band-ink);
    font-family: "Noto Sans JP", sans-serif;
    font-weight: 500;
    font-size: 20px;
    letter-spacing: 3px;
    display: flex; align-items: center; justify-content: center;
  }
  .label__story {
    position: absolute;
    left: 160px; top: 758px;
    width: 398px;
    margin: 0;
    text-align: center;
    font-family: "Lato", sans-serif;
    font-size: 10px;
    line-height: 28px;
    color: var(--ink-light);
  }
  .label__tone {
    position: absolute;
    left: 0; width: 718px; top: 900px;
    text-align: center;
    font-family: "Noto Sans JP", sans-serif;
    font-size: 12px;
    letter-spacing: 2px;
    color: var(--ink-light);
  }
</style>
</head>
<body>
<div class="label">
  <svg class="label__bottle" width="718" height="1200" viewBox="0 0 718 1200">
    <defs>
      <linearGradient id="scene" x1="0" y1="64" x2="0" y2="1178" gradientUnits="userSpaceOnUse">
        <stop offset="0" stop-color="var(--sky-deep)"/>
        <stop offset="0.3" stop-color="var(--sky-mid)"/>
        <stop offset="0.47" stop-color="var(--sky-pale)"/>
        <stop offset="0.5" stop-color="var(--ridge)"/>
        <stop offset="0.53" stop-color="var(--ridge-light)"/>
        <stop offset="0.56" stop-color="var(--lagoon)"/>
        <stop offset="0.78" stop-color="var(--lagoon-pale)"/>
        <stop offset="1" stop-color="var(--mist)"/>
      </linearGradient>
    </defs>
    <path role="img" aria-label="Photograph of a steaming blue geothermal lagoon under a blue sky with snowy mountains"
      d="M150 64 L570 64 Q626 66 628 124 L628 880 Q626 1060 592 1124 Q568 1174 500 1176 L220 1176 Q152 1174 128 1124 Q94 1060 92 880 L92 124 Q94 66 150 64 Z"
      fill="url(#scene)"/>
    <rect class="label__cap" x="151" y="18" width="418" height="80" rx="18" fill="var(--cap)" stroke="var(--cap-edge)" stroke-width="1.5"/>
  </svg>

  <div class="label__mark"></div>
  <h1 class="label__name label__name--first">AURORA</h1>
  <h1 class="label__name label__name--second">SERENE</h1>
  <div class="label__reading">オーロラ セレーネ</div>
  <div class="label__claim">シリカ＆酵素のチカラ</div>
  <p class="label__story">
    The world's largest hot spring with beautiful skin in Iceland<br>
    A bath salt with the image of a "mist haven"<br>
    It contains a lot of attention component "silica" as a beauty mineral.<br>
    The power of "enzyme" decomposes dirt on the body in the bathtub.
  </p>
  <div class="label__tone">湯色：ミルキーブルー（乳白色）</div>
</div>
</body>
</html>
```